Payment button (Check out) design

We need a logo design for a payment check out for an online retail store, www.trelvix.com. This payment check button should represent customer can check out via credit card and debit card, other than frobex check out.

Target Market(s)

UK

Industry/Entity Type

Digital Camera

Logo Text

Pay with credit/debit card (prefer in blue tone, consistent with our logo design)

Logo styles of interest
Wordmark Logo
Font styles to use
Serif
Sans Serif

Colors
0355a3
3176b5
85acd3
85cae6
33a6d7
0692cd

```html
<!DOCTYPE html>
<html lang="en">
<head>
<meta charset="utf-8">
<title>Pay with credit/debit card – checkout buttons</title>
<link rel="stylesheet" href="https://fonts.googleapis.com/css2?family=Oswald:wght@700&display=swap">
<style>
  :root {
    --page-bg: #ffffff;
    --pill-edge: #1a7fc0;
    --pill-top: #1c88c8;
    --pill-bottom: #1263a5;
    --pill-shine: #cfe0f1;
    --tab-edge: #1166ab;
    --tab-top: #0f6db2;
    --tab-bottom: #169cd7;
    --gloss-light: #f4f6fb;
    --gloss-deep: #9eb2d8;
    --label-light: #ffffff;
    --label-dark: #231f20;
  }
  html, body {
    margin: 0;
    padding: 0;
    width: 1200px;
    height: 960px;
    overflow: hidden;
    background: var(--page-bg);
  }
  .artboard {
    display: block;
    width: 1200px;
    height: 960px;
  }
  .button-label {
    font-family: "Oswald", "Arial Narrow", sans-serif;
    font-weight: 700;
    font-size: 80px;
    text-transform: uppercase;
  }
  .button-label--light { fill: var(--label-light); }
  .button-label--dark { fill: var(--label-dark); }
</style>
</head>
<body>
<svg class="artboard" viewBox="0 0 1200 960" xmlns="http://www.w3.org/2000/svg">
  <defs>
    <linearGradient id="pill-fill" x1="0" y1="0" x2="0" y2="1">
      <stop offset="0" stop-color="var(--pill-top)"/>
      <stop offset="1" stop-color="var(--pill-bottom)"/>
    </linearGradient>
    <linearGradient id="pill-shine" x1="0" y1="0" x2="0" y2="1">
      <stop offset="0" stop-color="var(--pill-shine)" stop-opacity="0.95"/>
      <stop offset="1" stop-color="var(--pill-shine)" stop-opacity="0"/>
    </linearGradient>
    <linearGradient id="tab-fill" x1="0" y1="0" x2="0" y2="1">
      <stop offset="0" stop-color="var(--tab-top)"/>
      <stop offset="1" stop-color="var(--tab-bottom)"/>
    </linearGradient>
    <linearGradient id="tab-gloss" x1="0" y1="0" x2="0" y2="1">
      <stop offset="0" stop-color="var(--gloss-light)"/>
      <stop offset="1" stop-color="var(--gloss-deep)"/>
    </linearGradient>
  </defs>

  <!-- Rounded pill checkout button -->
  <g class="checkout-button checkout-button--pill">
    <rect x="207" y="217" width="843" height="190" rx="95"
          fill="url(#pill-fill)" stroke="var(--pill-edge)" stroke-width="4"/>
    <path d="M212 312 C212 260 250 232 300 232 L955 232 C1005 232 1044 260 1044 312
             C1040 272 1005 248 960 248 L300 248 C255 248 218 272 212 312 Z"
          fill="url(#pill-shine)"/>
    <g transform="translate(630 342) skewX(-12)">
      <text class="button-label button-label--light" x="0" y="0" text-anchor="middle"
            textLength="780" lengthAdjust="spacingAndGlyphs">Pay with credit/debit card</text>
    </g>
  </g>

  <!-- Glossy tab checkout button -->
  <g class="checkout-button checkout-button--tab">
    <rect x="214" y="632" width="828" height="204" rx="48"
          fill="url(#tab-fill)" stroke="var(--tab-edge)" stroke-width="5"/>
    <path class="tab-gloss" d="M225 720 L225 680 Q225 642 263 642 L994 642 Q1032 642 1032 680 L1032 720 Z"
          fill="url(#tab-gloss)"/>
    <g transform="translate(630 765) skewX(-12)">
      <text class="button-label button-label--dark" x="0" y="0" text-anchor="middle"
            textLength="780" lengthAdjust="spacingAndGlyphs">Pay with credit/debit card</text>
    </g>
    <path d="M225 720 L225 680 Q225 642 263 642 L994 642 Q1032 642 1032 680 L1032 720 Z"
          fill="url(#tab-gloss)" opacity="0.4"/>
  </g>
</svg>
</body>
</html>
```